VKT Logistics Marketing flyer

Good morning, I run a trucking company and I will be needing help setting up a website logo and a marketing flyer or something like that talking about our services and what we can offer to potential new customers who need to ship their product. I need help getting this all together.

Target Market(s)

Transportation customers

Requirements
Must have
• should list our services and contact info
Nice to have
• the Logo on the top

```html
<!DOCTYPE html>
<html lang="en">
<head>
<meta charset="utf-8">
<title>VKT Logistics – Flyer</title>
<link href="https://fonts.googleapis.com/css2?family=Montserrat:wght@800;900&family=Poppins:ital,wght@0,400;0,500;0,600;0,700;1,600&display=swap" rel="stylesheet">
<style>
:root{
  --red:#e01b1b;
  --red-dark:#b81313;
  --navy:#1f3a7a;
  --ink:#111;
  --dark:#1c1c1c;
  --white:#fff;
  --gold:#f2b824;
  --grey:#555;
}
*{margin:0;padding:0;box-sizing:border-box}
html,body{width:896px;height:1200px;overflow:hidden;background:var(--white)}
body{font-family:'Poppins',sans-serif;color:var(--ink);position:relative}
.flyer{position:relative;width:896px;height:1200px;overflow:hidden;background:var(--white)}

.hero-photo{position:absolute;left:0;top:0;width:896px;height:642px;
  background:linear-gradient(180deg,#1d3577 0%,#2c4a8e 30%,#7a6a8a 48%,#d98a4a 62%,#b9562a 80%,#5a4a48 100%)}
.logo-plate{position:absolute;left:0;top:0;width:896px;height:100px}
.logo-name{position:absolute;left:0;width:896px;top:16px;text-align:center;font-family:'Poppins',sans-serif;font-weight:700;font-size:46px;line-height:1;color:var(--red)}
.logo-sub{position:absolute;left:0;width:896px;top:68px;text-align:center;font-weight:700;font-size:13px;letter-spacing:4px;color:var(--red)}

.headline{position:absolute;left:0;width:896px;text-align:center;font-family:'Montserrat',sans-serif;font-weight:900;line-height:1}
.headline.top{top:120px;font-size:52px;color:#f1f1f1;text-shadow:0 2px 3px rgba(0,0,0,.35)}
.headline.bottom{top:178px;font-size:55px;color:var(--red);text-shadow:0 2px 3px rgba(0,0,0,.3)}
.tagline{position:absolute;left:0;width:896px;top:242px;text-align:center;font-weight:600;font-size:24px;color:var(--white)}

.summary-wedge{position:absolute;left:0;top:580px;width:896px;height:70px}
.summary-title{position:absolute;left:63px;top:600px;font-weight:700;font-size:22px;line-height:1.1}
.summary-title span{color:var(--red)}
.summary-text{position:absolute;left:63px;top:661px;width:790px;font-weight:500;font-size:13px;line-height:1.2;color:#222}

.services{position:absolute;left:70px;top:708px;width:757px;height:166px;background:linear-gradient(180deg,#2a2a2a,#141414)}
.services-tab{position:absolute;left:238px;top:-12px;width:282px;height:32px;background:var(--red);clip-path:polygon(4% 0,96% 0,100% 100%,0 100%);color:var(--white);font-weight:600;font-size:20px;text-align:center;line-height:32px}
.service-list{position:absolute;left:55px;top:32px;display:flex;gap:33px}
.service{width:100px;text-align:center}
.service-photo{width:100px;height:66px;border-right:5px solid var(--red);transform:skewX(-6deg)}
.service-name{color:var(--white);font-weight:500;font-size:13px;line-height:1.05;margin-top:8px}
.services-foot{position:absolute;left:186px;bottom:0;width:385px;height:24px;background:var(--red);clip-path:polygon(4% 0,96% 0,100% 100%,0 100%);color:var(--white);font-weight:600;font-size:13px;text-align:center;line-height:24px}

.section-title{position:absolute;font-weight:600;font-size:18px}
.section-title span{color:var(--red)}
.testimonial{position:absolute;left:73px;width:358px;border:1px solid #333;padding:10px 10px 0 10px;font-size:11.5px;line-height:1.25}
.testimonial .quote-mark{position:absolute;left:10px;top:-14px;color:var(--red);font-family:'Montserrat',sans-serif;font-weight:900;font-size:24px;background:var(--white);padding:0 2px;line-height:1}
.testimonial .quote-end{position:absolute;color:var(--red);font-family:'Montserrat',sans-serif;font-weight:900;font-size:24px;background:var(--white);line-height:1}
.testimonial cite{display:block;font-style:italic;font-weight:600;margin-top:4px}

.customers{position:absolute;left:456px;top:926px;display:flex;gap:18px;align-items:center}
.customer-name{font-weight:600;font-size:16px;color:var(--navy)}

.award{position:absolute;display:flex;gap:10px;align-items:flex-start;font-weight:500;font-size:10.5px;line-height:1.2}
.award-badge{width:30px;height:30px;border-radius:50%;background:var(--gold);flex:none;margin-top:2px}

.closing{position:absolute;left:73px;top:1060px;width:760px;font-size:9.5px;line-height:1.25;color:var(--grey)}

.footer{position:absolute;left:0;top:1108px;width:896px;height:92px}
.contact{position:absolute;top:1120px;color:var(--white)}
.contact .name{font-weight:600;font-size:16px;line-height:1.2}
.contact .role{color:var(--red);font-weight:600;font-size:13px;line-height:1.2}
.contact .phone{display:flex;align-items:center;gap:4px;font-weight:600;font-size:13px;margin-top:2px}
.email{position:absolute;left:450px;top:1131px;display:flex;align-items:center;gap:8px;font-size:18px;color:#333}
.socials{position:absolute;left:722px;top:1134px;display:flex;gap:3px}
.socials span{width:20px;height:20px;border-radius:50%;background:var(--ink)}
</style>
</head>
<body>
<div class="flyer">

  <div class="hero-photo" role="img" aria-label="Orange semi-truck hauling red shipping containers through a port at sunset under a blue sky"></div>

  <svg class="logo-plate" viewBox="0 0 896 100" aria-hidden="true">
    <polygon points="285,0 611,0 563,100 333,100" fill="#fff"/>
  </svg>
  <div class="logo-name">VKT</div>
  <div class="logo-sub">LOGISTICS LLC</div>

  <h1 class="headline top">MAXIMIZING EFFICIENCY</h1>
  <h1 class="headline bottom">IN TRANSPORTATION</h1>
  <p class="tagline">Your Number One Call for Reliable Transportation Solutions</p>

  <svg class="summary-wedge" viewBox="0 0 896 70" aria-hidden="true">
    <polygon points="0,62 896,62 896,70 0,70" fill="#fff"/>
    <polygon points="0,7 385,7 433,62 0,62" fill="#fff"/>
    <polygon points="0,3 386,3 440,58 896,58 896,62 432,62 380,7 0,7" fill="#e01b1b"/>
  </svg>
  <h2 class="summary-title">Summary of VKT Logistics<br><span>LLC's services and expertise:</span></h2>
  <p class="summary-text">Specializing in dry van, reefer, flatbed, and tanker loads, we strive to provide efficient and safe transportation solutions for our customers.</p>

  <section class="services">
    <div class="services-tab">VKT Logistics LLC's services:</div>
    <div class="service-list">
      <div class="service"><div class="service-photo" role="img" aria-label="White cargo van on a city street" style="background:linear-gradient(135deg,#c9b9a3,#e8e8e8)"></div><div class="service-name">Dry van transportation</div></div>
      <div class="service"><div class="service-photo" role="img" aria-label="Blue refrigerated truck on the highway" style="background:linear-gradient(135deg,#7fb0e3,#1f47b8)"></div><div class="service-name">Reefer transportation</div></div>
      <div class="service"><div class="service-photo" role="img" aria-label="Flatbed truck on the road" style="background:linear-gradient(135deg,#9aa0a8,#e6dccb)"></div><div class="service-name">Flatbed transportation</div></div>
      <div class="service"><div class="service-photo" role="img" aria-label="Silver tanker truck on a highway" style="background:linear-gradient(135deg,#dfe3e8,#8d949b)"></div><div class="service-name">Tanker transportation</div></div>
      <div class="service"><div class="service-photo" role="img" aria-label="Two truck drivers talking beside their rigs" style="background:linear-gradient(135deg,#6c7f99,#2f4f7a)"></div><div class="service-name">Solo and team driver services</div></div>
    </div>
    <div class="services-foot">Adjusting to customer needs with fleet flexibility</div>
  </section>

  <h3 class="section-title" style="left:114px;top:886px"><span>SOME CUSTOMER</span> TESTIMONIALS:</h3>
  <blockquote class="testimonial" style="top:922px;height:56px">
    <span class="quote-mark">&#8220;</span>
    VKT Logistics LLC has been a reliable partner for our transportation needs.
    <cite>-Orvane Citrus Products</cite>
    <span class="quote-end" style="left:165px;top:42px">&#8221;</span>
  </blockquote>
  <blockquote class="testimonial" style="top:990px;height:54px;padding-top:14px">
    <span class="quote-mark">&#8220;</span>
    Their efficiency and customer service are unmatched.
    <cite>-Citrana North America</cite>
    <span class="quote-end" style="left:162px;top:40px">&#8221;</span>
  </blockquote>

  <h3 class="section-title" style="left:456px;top:886px">OUR CUSTOMERS</h3>
  <div class="customers">
    <span class="customer-name">Orvane</span>
    <span class="customer-name">Crispo Foods</span>
    <span class="customer-name">Citrana</span>
    <span class="customer-name">Novalo</span>
  </div>

  <h3 class="section-title" style="left:460px;top:964px"><span>AWARDS</span> AND RECOGNITION:</h3>
  <div class="award" style="left:460px;top:996px"><span class="award-badge"></span><span>Rallo Elite Carrier<br>Excellence Award<br>(2 years in a row)</span></div>
  <div class="award" style="left:598px;top:996px"><span class="award-badge"></span><span>Number one truck supplier to<br>two major orange juice<br>manufacturers in the US</span></div>

  <p class="closing">What sets us apart from any other carrier is that when you call you will get either the owner or the CFO, you will not have to wait for approvals and time wasted. We work through the problems to find the right solution then get it executed quickly and effectively.</p>

  <svg class="footer" viewBox="0 0 896 92" aria-hidden="true">
    <rect x="0" y="0" width="896" height="92" fill="#fff"/>
    <polygon points="0,0 390,0 438,86 896,86 896,92 0,92" fill="#e01b1b"/>
    <polygon points="0,0 382,0 430,92 0,92" fill="#1c1c1c"/>
  </svg>

  <div class="contact" style="left:110px">
    <div class="name">Dale Hartwell</div>
    <div class="role">CFO</div>
    <div class="phone"><svg width="14" height="14" viewBox="0 0 14 14"><circle cx="7" cy="7" r="7" fill="#e01b1b"/><path d="M4.5 3.5l1.5 0 .6 1.8-.9.7a5 5 0 002.3 2.3l.7-.9 1.8.6v1.5c0 .5-.4.8-.9.7A6.5 6.5 0 013.8 4.4c-.1-.5.2-.9.7-.9z" fill="#fff"/></svg>555-014-2271</div>
  </div>
  <div class="contact" style="left:256px">
    <div class="name">Jordan Pierce</div>
    <div class="role">CEO</div>
    <div class="phone"><svg width="14" height="14" viewBox="0 0 14 14"><circle cx="7" cy="7" r="7" fill="#e01b1b"/><path d="M4.5 3.5l1.5 0 .6 1.8-.9.7a5 5 0 002.3 2.3l.7-.9 1.8.6v1.5c0 .5-.4.8-.9.7A6.5 6.5 0 013.8 4.4c-.1-.5.2-.9.7-.9z" fill="#fff"/></svg>555-019-4836</div>
  </div>

  <div class="email"><svg width="20" height="20" viewBox="0 0 20 20"><circle cx="10" cy="10" r="10" fill="#e01b1b"/><rect x="5" y="6.5" width="10" height="7" fill="none" stroke="#fff" stroke-width="1.3"/><path d="M5 6.5l5 4 5-4" fill="none" stroke="#fff" stroke-width="1.3"/></svg>hello@vktfreight.net</div>
  <div class="socials" aria-label="Social media"><span></span><span></span><span></span></div>

</div>
</body>
</html>
```